Everything fresh, everything new

When I take over the practice, I would like to breathe new life into the practice. I want a business card design that catches the eye and brings a breath of fresh air

```html
<!DOCTYPE html>
<html lang="en">
<head>
<meta charset="utf-8">
<title>Vitalwerk – Business Cards</title>
<link href="https://fonts.googleapis.com/css2?family=Didact+Gothic&family=Roboto+Slab:wght@400;700&display=swap" rel="stylesheet">
<style>
  :root {
    --backdrop: #c9c8c4;
    --card: #ffffff;
    --green: #8cc63f;
    --green-soft: #a9d46a;
    --green-dark: #2f4a1c;
    --ink: #2b2b2b;
    --grey: #6e6e6e;
    --faint: #efefef;
    --rule: #b7dc86;
  }
  * { margin: 0; padding: 0; box-sizing: border-box; }
  html, body { width: 1200px; height: 801px; overflow: hidden; }
  body {
    background: var(--backdrop);
    display: flex;
    align-items: center;
    justify-content: center;
    gap: 50px;
  }
  .card {
    position: relative;
    width: 525px;
    height: 300px;
    background: var(--card);
    box-shadow: 0 6px 18px rgba(0,0,0,0.18);
    overflow: hidden;
  }

  /* Front: contact side */
  .card--front .watermark {
    position: absolute;
    left: 14px;
    bottom: 14px;
    font-family: "Didact Gothic", sans-serif;
    font-size: 112px;
    line-height: 1;
    color: var(--faint);
    white-space: nowrap;
    letter-spacing: 1px;
  }
  .front-content {
    position: relative;
    height: 100%;
    display: flex;
    flex-direction: column;
    align-items: center;
    padding-top: 42px;
  }
  .brand-name {
    font-family: "Didact Gothic", sans-serif;
    font-size: 30px;
    line-height: 1;
    color: var(--ink);
    letter-spacing: 0.5px;
  }
  .person {
    margin-top: 30px;
    text-align: center;
    font-family: "Roboto Slab", serif;
  }
  .person__name {
    font-weight: 700;
    font-size: 17px;
    color: var(--green-dark);
    border-bottom: 1px solid var(--green-dark);
    display: inline-block;
    line-height: 1.2;
  }
  .person__role {
    font-size: 12px;
    color: var(--ink);
    margin-top: 2px;
  }
  .contact {
    list-style: none;
    margin-top: 12px;
    text-align: center;
    font-family: "Roboto Slab", serif;
    font-size: 13px;
    line-height: 1.45;
    color: var(--ink);
  }

  /* Back: brand side */
  .card--back .back-content {
    position: absolute;
    inset: 0;
    display: flex;
    flex-direction: column;
    align-items: center;
    justify-content: center;
  }
  .back-brand {
    font-family: "Didact Gothic", sans-serif;
    font-size: 66px;
    color: var(--green-soft);
    letter-spacing: 1px;
    line-height: 1;
  }
  .back-web {
    display: flex;
    align-items: center;
    gap: 12px;
    margin-top: 14px;
    width: 400px;
  }
  .back-web .rule {
    flex: 1;
    height: 1px;
    background: var(--rule);
  }
  .back-web .url {
    font-family: "Roboto Slab", serif;
    font-size: 15px;
    color: var(--grey);
    letter-spacing: 1px;
  }
</style>
</head>
<body>
  <article class="card card--front">
    <div class="watermark" aria-hidden="true">Vitalwerk</div>
    <div class="front-content">
      <div class="brand-name">Vitalwerk</div>
      <div class="person">
        <div class="person__name">Jonas Keller</div>
        <div class="person__role">Directer</div>
      </div>
      <ul class="contact">
        <li>(555) 014 2267</li>
        <li>kontakt@vitalwerk.com</li>
        <li>vitalwerk.com</li>
        <li>Your Address, City</li>
      </ul>
    </div>
  </article>

  <article class="card card--back">
    <div class="back-content">
      <div class="back-brand">Vitalwerk</div>
      <div class="back-web">
        <span class="rule"></span>
        <span class="url">vitalwerk.com</span>
        <span class="rule"></span>
      </div>
    </div>
  </article>
</body>
</html>
```